Create a Wordpress Design (Delvo)

We need a wordpress design for an established auction and real estate company based in Tennessee. The winning design will incorporate a professional color scheme with company logo in a clean layout. The design needs to consider that this will be developed on a responsive theme. Colors are those that will highlight the logo.
Updates

This client, an older gentleman, wants the site to mimic http://www.pranketbids.example/. If you can adjust you designs with this site in mind - perhaps 3 columns, less color etc. We are trying to get him a concept that he likes and he keeps mentioning this site. Do not copy this site, but keep it in mind while re-doing the concept. Thanks, - auction services -

Industry/Entity Type

Real Estate

Font styles to use
Sans Serif

Colors

Designer to choose colors to be used in the design.

Requirements
Must have
• - Navigation: 1) Home - with auctions as content as seen at http://brindlehammerco.example/ 2) Properties for Sale 3) Auctions 4) Sell Your Property 5) Community Info 6) About Us 7) Contact Us

Color will be those that highlight logo in a professional creative way. Site tagline: "Our Signs are Everywhere". Site will have a slideshow - please use stock real estate image for the initial photo.

Widgets: 1) social media (FB twitter, linked In, Youtube, RSS) 2) News & Events blog, 3) testimonials 4) featured Property widget.

Footer will have contact info (below) smaller company logo, and the association logos attached, and contact info:
Phone: (615) 555-0147
Contacts: Marcy Delane-Ortt
Email: marketing@kentdelvo.example
Address: 14-C Harlow Court W, Murfreesboro, TN 37130

Nice to have
• use and styling of a dropdown menu: Under AUCTIONS, 1) Upcoming 2) Past

```html
<!DOCTYPE html>
<html lang="en">
<head>
<meta charset="utf-8">
<title>Delvo Commercial</title>
<link href="https://fonts.googleapis.com/css2?family=Mulish:ital,wght@0,400;0,600;1,400&display=swap" rel="stylesheet">
<style>
:root{
  --red:#d0121d;
  --taupe:#978d87;
  --taupe-dark:#8a817b;
  --panel:#f1f1f1;
  --line:#dcdcdc;
  --text:#444;
  --muted:#666;
  --white:#fff;
}
*{box-sizing:border-box;margin:0;padding:0}
html,body{width:695px;height:1200px;overflow:hidden;background:var(--white)}
body{position:relative;font-family:'Mulish',sans-serif;color:var(--text)}
.abs{position:absolute}
.brand{left:43px;top:10px;width:104px;height:46px;display:flex;align-items:center;gap:6px}
.brand-dot{width:14px;height:14px;border-radius:50%;background:var(--red)}
.brand-name{font-size:22px;font-weight:600;color:var(--red)}
.phone{right:43px;top:24px;font-size:13px;color:var(--muted)}
.phone b{color:var(--red);font-weight:400}
.nav{left:43px;top:62px;width:609px;height:24px;background:var(--taupe);display:flex;font-size:7.2px;color:var(--white);text-transform:uppercase;padding-left:2px;z-index:2}
.nav span{display:flex;align-items:center;padding:0 12px}
.nav .active{background:var(--red)}
.dropdown{left:192px;top:86px;width:62px;height:35px;background:var(--red);color:var(--white);font-size:6.5px;text-align:center;padding-top:6px;line-height:11px;text-transform:uppercase;z-index:3}
.hero{left:44px;top:91px;width:607px;height:209px;z-index:1;background:linear-gradient(180deg,#3c6fb8 0%,#8fb2d8 35%,#e8e3c8 55%,#6a7a4a 85%,#3f4d2c 100%)}
.dots{left:327px;top:281px;display:flex;gap:3px;z-index:2}
.dots i{width:8px;height:8px;border-radius:50%;background:var(--white);display:block}
.dots i.on{background:var(--red)}
.section-title{left:47px;top:330px;font-size:14px;color:#333;font-weight:400}
.section-title b{color:var(--red);font-weight:400}
.card{position:absolute;left:48px;width:389px;height:210px;border:1px solid var(--line);background:var(--white)}
.card-head{height:22px;background:#f6f6f6;border-bottom:1px solid var(--line);font-size:9.5px;padding:4px 8px;color:#333}
.thumb{position:absolute;left:8px;top:30px;width:101px;height:91px;border:1px solid #ccc}
.thumb.a{background:linear-gradient(#a9c3e0,#f3f1ec 50%,#b3a79b)}
.thumb.b{background:linear-gradient(#c6d8ea,#8c6b55 45%,#a8845f 75%,#6f8f4b)}
.card h3{position:absolute;left:120px;top:29px;font-size:11.5px;font-weight:400;color:var(--red)}
.card p{position:absolute;left:120px;top:48px;width:262px;font-size:7.3px;line-height:12.2px;color:var(--muted)}
.btns{position:absolute;left:117px;top:104px;display:flex;gap:6px}
.btn{height:18px;width:55px;font-size:7px;color:var(--white);background:var(--taupe);display:flex;align-items:center;justify-content:center;text-transform:uppercase}
.btn.red{background:var(--red)}
.live{position:absolute;left:10px;top:134px;width:366px;height:66px;background:var(--panel);border:1px solid var(--line);padding:5px 14px;font-size:6.8px;line-height:13.5px;color:var(--text)}
.live h4{font-size:11px;font-weight:400;color:var(--red);line-height:15px}
.live em{font-style:normal;color:var(--red)}
.bid{position:absolute;right:8px;top:23px;width:138px;height:22px;background:var(--taupe);color:var(--white);font-size:6.8px;display:flex;align-items:center;justify-content:center;text-transform:uppercase}
.pager{left:48px;top:1016px;width:87px;height:20px;border:1px solid var(--line);font-size:6.8px;display:flex;align-items:center;justify-content:center;gap:6px;color:#444}
.powered{left:333px;top:1010px;width:103px;height:34px;border:1px solid #aab;border-radius:2px;font-size:6.8px;color:#223c7a;padding:4px 6px;line-height:11px}
.powered b{font-size:9px;font-weight:600}
.widget{position:absolute;left:460px;width:193px;background:var(--panel);border:1px solid var(--line)}
.widget-head{height:24px;background:var(--red);color:var(--white);font-size:11px;padding:4px 10px}
.fp-img{position:absolute;left:12px;top:35px;width:170px;height:98px;background:linear-gradient(#b8cfe6,#c9b7a8 40%,#8a5a44 60%,#6e9a48 78%,#5e8b3a)}
.fp-addr{position:absolute;left:12px;top:140px;font-size:8.5px;color:var(--red)}
.fp-text{position:absolute;left:12px;top:152px;width:170px;font-size:7px;line-height:12.5px;color:var(--muted)}
.wbtn{position:absolute;left:12px;height:20px;width:80px;background:var(--taupe);color:var(--white);font-size:6.8px;display:flex;align-items:center;justify-content:center;text-transform:uppercase}
.news{position:absolute;left:8px;width:177px;border-bottom:1px solid var(--line);height:75px}
.news .img{position:absolute;left:0;top:0;width:42px;height:38px;background:linear-gradient(#bcd2e8,#9a6b52 55%,#6f9147)}
.news .date{position:absolute;left:52px;top:-1px;font-size:8.5px;color:var(--red)}
.news .txt{position:absolute;left:52px;top:11px;width:125px;font-size:7px;line-height:12.4px;color:var(--muted)}
.news .more{position:absolute;left:52px;top:56px;font-size:7px;color:#333}
.quote{position:absolute;left:12px;width:172px;font-size:7px;line-height:12.5px;color:var(--muted);font-style:italic}
.quote .mark{display:inline-block;width:14px;height:9px;margin-right:4px;vertical-align:-1px}
.quote cite{display:block;color:var(--red);margin-top:5px}
.footer{left:0;top:1063px;width:695px;height:137px;background:var(--taupe-dark);color:var(--white)}
.footer h5{position:absolute;font-size:8.5px;font-weight:400}
.flinks{position:absolute;left:43px;top:33px;font-size:6.8px;line-height:13.4px}
.fbrand{position:absolute;left:149px;top:36px;display:flex;align-items:center;gap:5px;font-size:12px;font-weight:600;color:var(--white)}
.fbrand i{display:block;width:9px;height:9px;border-radius:50%;background:var(--red)}
.fcontact{position:absolute;left:148px;top:62px;font-size:6.8px;line-height:12.6px}
.assoc{position:absolute;left:357px;top:35px;width:296px;height:30px;background:var(--white);display:flex;align-items:center;justify-content:space-around;padding:0 4px}
.assoc i{display:block;background:#333}
.social{position:absolute;left:357px;top:98px;display:flex;gap:4px}
.social i{display:block;width:16px;height:16px;border-radius:2px}
.copy{position:absolute;left:512px;top:99px;font-size:6.4px;line-height:11px}
</style>
</head>
<body>

<div class="abs brand"><span class="brand-dot"></span><span class="brand-name">Delvo</span></div>
<div class="abs phone">Phone: <b>(615) 555-0147</b></div>

<nav class="abs nav">
  <span>Home</span><span>Properties for Sale</span><span class="active">Auctions</span><span>Sell Your Property</span><span>Community Info</span><span>About Us</span><span>Contact Us</span>
</nav>

<div class="abs hero" role="img" aria-label="Slideshow photo of a cream two-storey house with dark shutters under a blue sky"></div>
<div class="abs dropdown">Upcoming<br>Past</div>
<div class="abs dots"><i class="on"></i><i></i><i></i><i></i></div>

<h2 class="abs section-title">Featured <b>Auctions</b></h2>

<article class="card" style="top:355px">
  <div class="card-head">Real Estate Auction</div>
  <div class="thumb a" role="img" aria-label="Photo of a large white residential home"></div>
  <h3>Residential Home</h3>
  <p>Aliquam molestie, mi et imperdiet euismod, dui purus auctor tellus, et interdum lacus lectus et ante. Sed accumsan sollicitudin sapien, sit amet adipiscing turpis gravida ac. In congue, neque ac lobortis volutpat, libero mauris varius mi, vitae suscipit ipsum ligula vitae risus.</p>
  <div class="btns"><span class="btn">Details</span><span class="btn red">Photos</span><span class="btn red">Videos</span></div>
  <div class="live"><h4>Live On-Site Auction</h4><em>Began:</em> Saturday, October 05, 2013 at 10:00 AM EDT<br><em>Location:</em> 2210 Fenmore Circle<br>Zanesville, OH 43701<span class="bid">Click here for online bidding</span></div>
</article>

<article class="card" style="top:572px">
  <div class="card-head">Real Estate Auction</div>
  <div class="thumb b" role="img" aria-label="Photo of a brick residential home"></div>
  <h3>Residential Home</h3>
  <p>Aliquam molestie, mi et imperdiet euismod, dui purus auctor tellus, et interdum lacus lectus et ante. Sed accumsan sollicitudin sapien, sit amet adipiscing turpis gravida ac. In congue, neque ac lobortis volutpat, libero mauris varius mi, vitae suscipit ipsum ligula vitae risus.</p>
  <div class="btns"><span class="btn">Details</span><span class="btn red">Photos</span><span class="btn red">Videos</span></div>
  <div class="live"><h4>Live On-Site Auction</h4><em>Began:</em> Saturday, October 05, 2013 at 10:00 AM EDT<br><em>Location:</em> 2210 Fenmore Circle<br>Zanesville, OH 43701<span class="bid">Click here for online bidding</span></div>
</article>

<article class="card" style="top:791px">
  <div class="card-head">Real Estate Auction</div>
  <div class="thumb b" role="img" aria-label="Photo of a brick residential home"></div>
  <h3>Residential Home</h3>
  <p>Aliquam molestie, mi et imperdiet euismod, dui purus auctor tellus, et interdum lacus lectus et ante. Sed accumsan sollicitudin sapien, sit amet adipiscing turpis gravida ac. In congue, neque ac lobortis volutpat, libero mauris varius mi, vitae suscipit ipsum ligula vitae risus.</p>
  <div class="btns"><span class="btn">Details</span><span class="btn red">Photos</span><span class="btn red">Videos</span></div>
  <div class="live"><h4>Live On-Site Auction</h4><em>Began:</em> Saturday, October 05, 2013 at 10:00 AM EDT<br><em>Location:</em> 2210 Fenmore Circle<br>Zanesville, OH 43701<span class="bid">Click here for online bidding</span></div>
</article>

<div class="abs pager"><span>‹‹ PREV</span><span>|</span><span>NEXT ››</span></div>
<div class="abs powered">powered by:<br><b>Bidwell Services</b></div>

<aside class="widget" style="top:333px;height:219px">
  <div class="widget-head">Featured Property</div>
  <div class="fp-img" role="img" aria-label="Photo of a brick house on a green lawn"></div>
  <div class="fp-addr">4820 Ashgrove Cove, Murfreesboro, TN</div>
  <div class="fp-text">Aliquam molestie, mi et imperdiet euismod, dui purus auctor tellus, et interdum lacus lectus...</div>
  <span class="wbtn" style="top:188px">More Property</span>
</aside>

<aside class="widget" style="top:563px;height:217px">
  <div class="widget-head">News &amp; Events</div>
  <div class="news" style="top:37px"><div class="img" role="img" aria-label="News photo of a house"></div><span class="date">Aug 16, 2014</span><div class="txt">Aliquam molestie, mi et imperdiet euismod, dui purus auctor tellus, et interdum lacus lectus...</div><span class="more">Read More ››</span></div>
  <div class="news" style="top:112px"><div class="img" role="img" aria-label="News photo of a house"></div><span class="date">Aug 16, 2014</span><div class="txt">Aliquam molestie, mi et imperdiet euismod, dui purus auctor tellus, et interdum lacus lectus...</div><span class="more">Read More ››</span></div>
  <span class="wbtn" style="top:188px">Read All News</span>
</aside>

<aside class="widget" style="top:792px;height:200px">
  <div class="widget-head">Testimonials</div>
  <div class="quote" style="top:35px"><svg class="mark" viewBox="0 0 14 9"><circle cx="3.5" cy="5" r="3.5" fill="#bbb"/><circle cx="10.5" cy="5" r="3.5" fill="#bbb"/></svg>Aliquam molestie, mi et imperdiet euismod, dui purus auctor tellus, et interdum lacus lectus et ante. Sed accumsan sollicitudin sapien, sit amet adipiscing turpis gravida ac....<cite>-Corin Hallett</cite></div>
  <div class="quote" style="top:118px"><svg class="mark" viewBox="0 0 14 9"><circle cx="3.5" cy="5" r="3.5" fill="#bbb"/><circle cx="10.5" cy="5" r="3.5" fill="#bbb"/></svg>Aliquam molestie, mi et imperdiet euismod, dui purus auctor tellus, et interdum lacus lectus et ante. Sed accumsan sollicitudin sapien, sit amet adipiscing turpis gravida ac....<cite>-Corin Hallett</cite></div>
</aside>

<footer class="abs footer">
  <h5 style="left:43px;top:20px">Company</h5>
  <div class="flinks">Home<br>Properties for Sale<br>Auctions<br>Sell Your Property<br>&nbsp;Community Info<br>About Us<br>Contact Us</div>
  <h5 style="left:148px;top:20px">Contact Us</h5>
  <div class="fbrand"><i></i>Delvo</div>
  <div class="fcontact">Contacts: Marcy Delane-Ortt<br>Address: 14-C Harlow Court W, Murfreesboro, TN 37130<br><br>Phone: (615) 555-0147<br>Email: marketing@kentdelvo.example</div>
  <h5 style="left:357px;top:20px">Associated with</h5>
  <div class="assoc" role="img" aria-label="Association membership badges">
    <i style="width:30px;height:24px"></i><i style="width:28px;height:20px"></i><i style="width:20px;height:20px;border-radius:50%"></i><i style="width:22px;height:22px;border-radius:50%;background:#2a5aa8"></i><i style="width:34px;height:14px;border-radius:50%"></i><i style="width:22px;height:22px;border-radius:50%"></i><i style="width:36px;height:20px"></i><i style="width:26px;height:26px"></i>
  </div>
  <h5 style="left:357px;top:84px">Connect Us</h5>
  <div class="social"><i style="background:#3b5998"></i><i style="background:#3fa9e0"></i><i style="background:#1f6fb2"></i><i style="background:#f08a1d"></i><i style="background:#d9251d"></i></div>
  <div class="copy">Copyright © 2014 .Kentdelvo.All Right Reserved<br>Privacy Policy</div>
</footer>

</body>
</html>
```